VistaWave webpage - Design only no coding required

Please refer to "web content" uploaded 23rd Sep for content

We are a digital signage company based in Jakarta, Indonesia.

Our core business is placement of LCD Tv's in waiting rooms of various hospitals in Indonesia which plays educational videos regarding various health topics (prescription/ethical medicines), OTC drugs TVC and other FMCG and ads.

Our client portfolio consists of the worlds biggest and well known Pharmaceutical companies and also local pharmaceutical companies.

Other parts of our business are as follows:
- Patient symposiums
- Booths for product activation
- Queuing systems that we have developed in house that use an android tablet and connect to our TV's
- Branding. eg. Lift doors, banners (static signage)
- Hospital management software. Specially developed software that comes in a generic format and needs to be customized to suit each hospital. It manages everything for phone/web booking, queues, registration, patient records, doctors schedules, referrals, pharmacy and inventory and checkout/payments.

We are after a website redesign that is visually attractive and modern as we also deal with many advertising agencies.

Our logo is orange and black, however the black & white can be reversed if necessary.

Pages will need to be available in English & Bahasa Indonesia language formats.

I am happy to answer any questions asap, i can be contacted at info@vistawave.example.co.id

current site (www.vistawave.example.co.id)

Target Market(s)

Mainly our business is B2B dealing with advertising clients either directly or through ad agencies.

The other aspect of our target market is hospitals where we place our screens.

There is (but not largely) and consumer audience.

In summary:
We have the following target markets:
1. Advertisers/ad agencies
2. Hospitals that wish to use our business model to display content to their patients 3. We are in a developing country however most of our viewers and clients are from a high demographic profile

Industry/Entity Type

Pharmaceutical

Requirements
Must have
• We will require duplicates of the pages in English & Bahasa Indonesia

I would like the initial designs with a focus on being clean yet bold and emphasis on typography.

The following pages will be required (but not limited to) to qualify for the prize:

-Home

- About Us

- Services
(sub pages)
=Digital Signage
=Video Content Production
=Hospital Branding
=Event Management
=Seminar
=Queue System
=Hospital Management Software

-Why Choose Us?

- Contact Us

- Clients & Partners

- Gallery

Based on the "Nice to haves" site examples we do not necessarily require pictures of our LCD's/content on the main page(s) and would be happy to purchase required stock photos if needed/agreed.

We definitely want a modern feel and do not wish to overload with too much info on the main page.

(Please note the text in the attached file will most likely be changed once we have a design concept, probably less text)

Webpages we like:
http://www.plumbrookstudio.example.com/
http://kettlefinch.example.com

Nice to have
• This is some of the international players which we want our site to look like:
www.skylarkdisplays.example.com.au
http://www.marvellepanels.example.co.uk/
www.tundralens.example.com/

Should not have
• We prefer not to have old outdated fonts and a website that resembles anything like the current one, we are after a modern and professional feel.
These are some of our relative competitors of which we DO NOT want our website looking like but as a reference:
http://quillcare-global.example.com/index.html
http://rtb.example.co.id/

```html
<!DOCTYPE html>
<html lang="en">
<head>
<meta charset="utf-8">
<title>VistaWave — Home</title>
<link rel="stylesheet" href="https://fonts.googleapis.com/css2?family=Josefin+Sans:wght@300;400&family=Open+Sans:wght@400&family=Arimo:wght@400;700&display=swap">
<style>
  :root {
    --orange: #ffa200;
    --ink: #111111;
    --heading-dark: #3a3a40;
    --body-grey: #a7a2b3;
    --slate: #3d434c;
    --cream: #fff5e3;
    --rule: #eeeeee;
    --white: #ffffff;
  }
  * { margin: 0; padding: 0; box-sizing: border-box; }
  html, body { width: 1200px; height: 1000px; overflow: hidden; background: var(--white); }
  body { position: relative; font-family: "Open Sans", sans-serif; }

  .site-header { position: absolute; left: 0; top: 0; width: 1200px; height: 159px; background: var(--white); }
  .brand { position: absolute; left: 18px; top: 44px; display: flex; align-items: center; gap: 12px; }
  .brand-mark { width: 46px; height: 46px; background: var(--orange); }
  .brand-name { font-family: "Arimo", sans-serif; font-weight: 700; font-size: 34px; color: var(--ink); letter-spacing: -0.5px; }

  .main-nav { font-family: "Arimo", sans-serif; font-size: 15px; color: var(--ink); }
  .nav-item { position: absolute; top: 50px; height: 34px; line-height: 34px; white-space: nowrap; }
  .nav-item.is-active { left: 453px; width: 67px; text-align: center; background: var(--orange); color: var(--white); }
  .nav-item.is-active::after { content: ""; position: absolute; left: 50%; bottom: -6px; margin-left: -6px; border: 6px solid transparent; border-bottom: 0; border-top-color: var(--orange); }
  .nav-about { left: 540px; }
  .nav-services { left: 635px; }
  .nav-why { left: 726px; }
  .nav-contact { left: 872px; }
  .nav-clients { left: 975px; }
  .nav-gallery { left: 1125px; }
  .nav-caret { position: absolute; left: 50%; top: 40px; margin-left: -3px; font-size: 9px; line-height: 1; }

  .hero { position: absolute; left: 0; top: 159px; width: 1200px; height: 339px; }
  .hero-photo { position: absolute; inset: 0; background: linear-gradient(90deg, #4b4b4b 0%, #8a8a8a 30%, #bdbdbd 50%, #8d8d8d 75%, #5a5a5a 100%); }
  .hero-title { position: absolute; left: 529px; top: 135px; width: 649px; height: 123px; background: var(--orange); text-align: right; padding-right: 36px; font-family: "Josefin Sans", sans-serif; font-weight: 300; white-space: nowrap; }
  .hero-title h1 { font-weight: 300; font-size: 54px; color: var(--white); line-height: 1; padding-top: 20px; }
  .hero-title p { font-size: 26px; color: var(--heading-dark); line-height: 1; margin-top: 8px; }
  .slider-controls { position: absolute; left: 395px; top: 259px; width: 134px; height: 67px; background: var(--slate); }
  .hero-caption { position: absolute; left: 529px; top: 259px; width: 499px; height: 67px; background: var(--cream); padding: 17px 29px; font-family: "Josefin Sans", sans-serif; font-size: 11px; line-height: 15px; color: #a09a90; text-transform: uppercase; white-space: nowrap; }

  .section-title { font-family: "Josefin Sans", sans-serif; font-weight: 300; text-transform: uppercase; white-space: nowrap; }
  .body-copy { font-size: 13.5px; line-height: 24px; color: var(--body-grey); white-space: nowrap; }

  .welcome { position: absolute; left: 13px; top: 530px; width: 740px; }
  .welcome .section-title { font-size: 36px; color: var(--orange); line-height: 46px; }
  .welcome h3 { font-family: "Josefin Sans", sans-serif; font-weight: 300; font-size: 23px; color: var(--heading-dark); text-transform: uppercase; margin: 20px 0 0 3px; white-space: nowrap; }
  .welcome .body-copy { margin: 30px 0 0 3px; }
  .btn-read-more { position: absolute; left: 3px; top: 303px; width: 109px; height: 44px; background: var(--orange); color: var(--white); font-family: "Josefin Sans", sans-serif; font-size: 15px; line-height: 46px; text-align: center; }
  .divider { position: absolute; left: 13px; top: 925px; width: 738px; height: 1px; background: var(--rule); }
  .projects-title { position: absolute; left: 13px; top: 972px; font-size: 28px; color: var(--heading-dark); line-height: 36px; }

  .services { position: absolute; left: 786px; top: 530px; width: 400px; }
  .services > .section-title { font-size: 29px; color: var(--heading-dark); line-height: 36px; }
  .service { margin-left: 24px; }
  .service h4 { font-family: "Josefin Sans", sans-serif; font-weight: 300; font-size: 18px; color: var(--orange); text-transform: uppercase; line-height: 24px; white-space: nowrap; }
  .service .body-copy { margin-top: 16px; }
  .service-signage { margin-top: 28px; }
  .service-video { margin-top: 14px; }
  .service-branding { margin-top: 18px; }
</style>
</head>
<body>
  <header class="site-header">
    <div class="brand"><span class="brand-mark"></span><span class="brand-name">VistaWave</span></div>
    <nav class="main-nav">
      <span class="nav-item is-active">Home</span>
      <span class="nav-item nav-about">About Us</span>
      <span class="nav-item nav-services">Services<span class="nav-caret">↓</span></span>
      <span class="nav-item nav-why">Why Choose Us?</span>
      <span class="nav-item nav-contact">Contact Us</span>
      <span class="nav-item nav-clients">Clients &amp; Partners</span>
      <span class="nav-item nav-gallery">Gallery</span>
    </nav>
  </header>

  <section class="hero">
    <div class="hero-photo" role="img" aria-label="Hospital waiting room corridor with wall-mounted LCD screens and rows of seats"></div>
    <div class="hero-title">
      <h1>VISTAWAVE PROVIDES</h1>
      <p>HIGH DEFINATION LCD SCREENS</p>
    </div>
    <div class="slider-controls">
      <svg width="134" height="67" viewBox="0 0 134 67">
        <polyline points="39,23 29,34 39,45" fill="none" stroke="#d8dce2" stroke-width="1.5"/>
        <polyline points="95,23 105,34 95,45" fill="none" stroke="#d8dce2" stroke-width="1.5"/>
      </svg>
    </div>
    <div class="hero-caption">We provide high definition LCD screens in hospital waiting rooms<br>for patient viewing.</div>
  </section>

  <section class="welcome">
    <h2 class="section-title">Welcome to our site</h2>
    <h3>Here is a little about us.</h3>
    <p class="body-copy">VistaWave was established to facilitate direct to customer marketing opportunities, especially within the<br>healthcare sphere. Our digital signage system uses the latest technology &amp; software to deliver reliable &amp;<br>effective content to its viewers in a highly segmented manner.<br>We encourage our clients to create patient awareness and knowledge of various health related topics<br>with the vision to creating an improved quality of life and a healthy lifestyle as they say “prevention is<br>better than the cure”.</p>
    <span class="btn-read-more">READ MORE</span>
  </section>
  <div class="divider"></div>
  <h2 class="section-title projects-title">Latest Projects</h2>

  <section class="services">
    <h2 class="section-title">Our Services</h2>
    <article class="service service-signage">
      <h4>Digital Signage</h4>
      <p class="body-copy">A network of LCD televisions are strategically placed in<br>various clinic waiting rooms in Hospitals. Our focus has<br>been on class A &amp; B hospitals however we have continu-<br>ously increased our span to cover more hospitals.</p>
    </article>
    <article class="service service-video">
      <h4>Video Content Production</h4>
      <p class="body-copy">We understand clients may not have content ready for<br>marketing nor do they have the time and experience to<br>arrange it. As a value-added service VistaWave bridges<br>the gap between idea conception and final video deliv-<br>ery.</p>
    </article>
    <article class="service service-branding">
      <h4>Hospital Branding</h4>
      <p class="body-copy">Our strong relationships with all our partner Hospitals<br>allow us to easily and quickly arrange placement oppor-<br>tunities.</p>
    </article>
  </section>
</body>
</html>
```